New Zealand Export company needs business cards

We need new business cards to match our new logo for a company based in New Zealand who deal specifically with the Pacific Islands. We source, consolidate and ship products out of New Zealand to the Pacific Islands. Will attach our old ones and also new logo.
Would like the Islands we deal with and the areas of work we have access to, to be included on the business cards.

Contact Information for Business Card

T +64 9 571 3048
F +64 9 571 6285
12-18 Kowhai Lane, Kerewai Flats, 9731
PO Box 814, Kerewai Flats, Tawhiri 9738, New Zealand
www.falconfreight.example.nz
E sales@falconfreight.example.nz

Font styles to use
Sans Serif

Colors
85abd2
33a6d7
ffffff

Requirements
Must have
• A company of PWM

```html
<!DOCTYPE html>
<html lang="en">
<head>
<meta charset="utf-8">
<title>Falcon Freight – Business Cards</title>
<link href="https://fonts.googleapis.com/css2?family=PT+Sans:ital,wght@0,400;0,700;1,700&display=swap" rel="stylesheet">
<style>
  :root {
    --stage: #1c1c1e;
    --card: #272729;
    --blue: #33a6d7;
    --blue-soft: #85abd2;
    --white: #ffffff;
    --muted: #e6e6e6;
  }
  * { box-sizing: border-box; margin: 0; padding: 0; }
  html, body { width: 1200px; height: 1200px; overflow: hidden; }
  body {
    background: var(--stage);
    font-family: "PT Sans", Arial, sans-serif;
    position: relative;
  }
  .card {
    position: absolute;
    width: 640px;
    height: 366px;
    background: var(--card);
    border-radius: 4px;
    box-shadow: 0 18px 40px rgba(0,0,0,.55);
  }
  .card--front { left: 110px; top: 150px; }
  .card--back { left: 450px; top: 660px; }

  .brand {
    position: absolute;
    display: flex;
    align-items: center;
    gap: 14px;
    white-space: nowrap;
  }
  .brand__square { width: 26px; height: 26px; background: var(--blue-soft); flex: none; }
  .brand__name {
    color: var(--blue);
    font-weight: 700;
    font-size: 40px;
    letter-spacing: 2px;
    text-transform: uppercase;
    line-height: 1;
    white-space: nowrap;
  }
  .card--front .brand { left: 50%; top: 150px; transform: translateX(-50%); }
  .front__web {
    position: absolute;
    left: 0; right: 0; bottom: 46px;
    text-align: center;
    color: var(--blue);
    font-weight: 700;
    font-style: italic;
    font-size: 17px;
  }

  .card--back .brand { left: 40px; top: 165px; gap: 12px; }
  .card--back .brand__square { width: 22px; height: 22px; }
  .card--back .brand__name { font-size: 29px; letter-spacing: 1.5px; }
  .back__divider {
    position: absolute;
    left: 370px; top: 60px;
    width: 2px; height: 200px;
    background: var(--blue);
  }
  .contact {
    position: absolute;
    left: 392px; top: 56px;
    color: var(--white);
    white-space: nowrap;
  }
  .contact__name {
    color: var(--blue);
    font-size: 23px;
    text-transform: uppercase;
    line-height: 1.1;
  }
  .contact__role { font-size: 16px; margin-bottom: 10px; color: var(--muted); }
  .contact__address { font-size: 14px; line-height: 1.3; margin-bottom: 10px; }
  .contact__list { list-style: none; font-size: 14px; line-height: 1.35; }
  .contact__list li { display: flex; align-items: center; gap: 8px; }
  .contact__list svg { width: 12px; height: 12px; flex: none; }
  .parent {
    position: absolute;
    left: 28px; bottom: 26px;
    color: var(--blue);
  }
  .parent__label { font-size: 11px; }
  .parent__name { font-size: 18px; font-weight: 700; letter-spacing: 3px; line-height: 1.1; }
  .parent__full { font-size: 7px; text-transform: uppercase; letter-spacing: .5px; }
</style>
</head>
<body>
  <section class="card card--front">
    <div class="brand">
      <span class="brand__square"></span>
      <span class="brand__name">Falcon Freight</span>
    </div>
    <p class="front__web">www.falconfreight.example.nz</p>
  </section>

  <section class="card card--back">
    <div class="brand">
      <span class="brand__square"></span>
      <span class="brand__name">Falcon Freight</span>
    </div>
    <span class="back__divider"></span>
    <div class="contact">
      <p class="contact__name">Tessa Harlow</p>
      <p class="contact__role">Sales Manager</p>
      <p class="contact__address">12-18 Kowhai Lane, Kerewai Flats<br>9731 PO Box 814, Kerewai Flats<br>Tawhiri 9738, New Zealand</p>
      <ul class="contact__list">
        <li><svg viewBox="0 0 12 12"><rect x="3" y="0.5" width="6" height="11" rx="1" fill="none" stroke="#33a6d7" stroke-width="1.2"/><circle cx="6" cy="9.5" r=".7" fill="#33a6d7"/></svg>+64 9 571 6285</li>
        <li><svg viewBox="0 0 12 12"><path d="M2.5 1 L4.5 1 L5.5 3.5 L4 4.6 C4.6 6 6 7.4 7.4 8 L8.5 6.5 L11 7.5 L11 9.5 C11 10.3 10.3 11 9.5 11 C5 11 1 7 1 2.5 C1 1.7 1.7 1 2.5 1 Z" fill="#33a6d7"/></svg>+64 9 571 3048</li>
        <li><svg viewBox="0 0 12 12"><rect x="1" y="2.5" width="10" height="7" fill="#33a6d7"/><path d="M1 2.5 L6 6.5 L11 2.5" fill="none" stroke="#272729" stroke-width="1"/></svg>sales@falconfreight.example.nz</li>
        <li><svg viewBox="0 0 12 12"><circle cx="6" cy="6" r="5" fill="none" stroke="#33a6d7" stroke-width="1.1"/><ellipse cx="6" cy="6" rx="2.2" ry="5" fill="none" stroke="#33a6d7" stroke-width=".9"/><path d="M1 6 H11" stroke="#33a6d7" stroke-width=".9"/></svg>www.falconfreight.example.nz</li>
      </ul>
    </div>
    <div class="parent">
      <p class="parent__label">A company of</p>
      <p class="parent__name">PWM</p>
      <p class="parent__full">Pacific Wharf Merchants</p>
    </div>
  </section>
</body>
</html>
```